Life Coach business needs a website design

I would like to get support in creating a website design. I will be starting a business as a life coach and I would like to start with something basic, but chic. It will be mainly a blog for now, but then I would like to start adding videos and hopefully podcast in the future. I took professional pictures of myself that I would like to include as a cover page. My main goal with this website is to capture the right audience by connecting with them through my mission, which is to embrace their inner greatness. I want to provide a sense of love, courage and authenticity when they open my website. I have a domain in Pagewell called :"Unfold the hidden bloom". I would be happy to discuss more of the details over the phone.

Target Market(s)

Young Adults (25-35)

Number of Pages Required

4 page

Colors

Designer to choose colors to be used in the design.

Requirements
Must have
• I am looking for a similar layout and vibe to these websites: https://tessawhorlby.com/meet-tessa/
• https://www.junopraskett.com
• My home page will include: About, Blog, Podcast, Subscribe.. (We can add icons of snapverra, clipvane and Boardlyn)
• I would like to have my name in the middle (Lunet), and include a note next to my picture "Your life is like a blank canvas and only you have the power to transform it into masterpiece. Take a chance and unfold the hidden bloom" L.T.

```html
<!DOCTYPE html>
<html lang="en">
<head>
<meta charset="utf-8">
<title>Lunet — Life Coach</title>
<link href="https://fonts.googleapis.com/css2?family=Cormorant+Garamond:ital,wght@0,400;0,500;1,400&family=Lato:wght@300;400;700&display=swap" rel="stylesheet">
<style>
:root{
  --ink:#1c1c1c;
  --text:#555555;
  --muted:#8a8a8a;
  --line:#e4e4e4;
  --paper:#ffffff;
  --band:#f4f4f4;
  --footer:#232323;
  --blush:#e9cfc8;
  --sea:#a9bfcc;
  --sand:#cfc4b4;
}
*{margin:0;padding:0;box-sizing:border-box}
html,body{width:1200px;height:4637px;overflow:hidden;background:var(--paper)}
body{position:relative;font-family:'Lato',sans-serif;color:var(--text)}
.abs{position:absolute}
.serif{font-family:'Cormorant Garamond',serif;color:var(--ink);font-weight:400}
.photo{position:absolute}
.body-copy{font-size:14px;line-height:25px;font-weight:300;color:var(--text)}

/* nav */
.nav{left:0;top:22px;width:1200px;height:24px}
.nav a{position:absolute;font-size:13px;letter-spacing:2px;color:var(--ink);text-decoration:none;transform:translateX(-50%)}
.rule{left:45px;top:63px;width:1110px;height:1px;background:var(--line)}

/* hero */
.hero-card{left:180px;top:389px;width:842px;height:235px;background:rgba(255,255,255,.82)}
.brand{left:0;width:1200px;top:318px;text-align:center;font-size:92px;line-height:1}
.quote{left:180px;width:842px;top:436px;text-align:center;font-family:'Cormorant Garamond',serif;font-style:italic;font-size:34px;line-height:47px;color:var(--ink)}
.cite{left:180px;width:842px;top:578px;text-align:center;font-size:13px;color:var(--muted)}

.band{left:0;width:1200px;background:var(--band)}
h2.serif{position:absolute;font-size:56px;line-height:1}
h3.serif{position:absolute;font-size:36px;line-height:1}

.btn{position:absolute;width:184px;height:40px;border:1.5px solid var(--ink);font-size:10px;font-weight:700;letter-spacing:1.5px;color:var(--ink);display:flex;align-items:center;justify-content:center}
.btn.solid{background:var(--ink);color:#fff}

.social{display:flex;gap:22px;align-items:center;font-size:13px;color:var(--ink)}
.social span{display:flex;align-items:center;gap:7px}
.social i{display:block;width:16px;height:16px;border-radius:50%;background:var(--ink)}
.social.light{color:#fff}
.social.light i{background:#fff}

.field{position:absolute;left:588px;top:4293px;width:294px;height:40px;background:#fff;font-size:10px;letter-spacing:1.5px;color:var(--muted);display:flex;align-items:center;padding-left:42px}

.footer{left:0;top:4433px;width:1200px;height:204px;background:var(--footer)}
.footer-links{left:140px;top:4508px;font-size:9px;letter-spacing:1.5px;line-height:20px;color:#6f6f6f}
</style>
</head>
<body>

<nav class="abs nav">
  <a style="left:392px">ABOUT</a>
  <a style="left:507px">BLOG</a>
  <a style="left:635px">PODCAST</a>
  <a style="left:784px">SUBSCRIBE</a>
</nav>
<div class="abs rule"></div>

<header>
  <div class="photo" role="img" aria-label="Portrait of the coach in a blush dress seated on seaside rocks" style="left:45px;top:104px;width:540px;height:600px;background:linear-gradient(160deg,#7d8b93 0%,#a9a49b 35%,var(--blush) 70%,#b8ad9f 100%)"></div>
  <div class="photo" role="img" aria-label="The coach in a flowing blush dress against sky and sea" style="left:615px;top:104px;width:540px;height:600px;background:linear-gradient(180deg,#dfe6ea 0%,var(--sea) 45%,var(--blush) 70%,#a89c8a 100%)"></div>
  <div class="abs hero-card"></div>
  <h1 class="abs serif brand">Lunet</h1>
  <p class="abs quote">“Your life is like a blank canvas and only you have<br>the power to transform it into masterpiece. Take a<br>chance and unfold the hidden bloom”</p>
  <p class="abs cite">– L.T.</p>
</header>

<section>
  <div class="abs band" style="top:745px;height:542px"></div>
  <h2 class="serif" style="left:140px;top:860px">About</h2>
  <p class="abs body-copy" style="left:140px;top:942px;width:450px">Lorem ipsum dolor sit amet, consectetur adipisicing elit, sed do eiusmod tempor incididunt ut labore et dolore magna aliqua. Ut enim ad minim veniam, quis nostrud exercitation ullamco laboris nisi ut aliquip ex ea commodo consequat.</p>
  <p class="abs body-copy" style="left:140px;top:1068px;width:450px">Lorem ipsum dolor sit amet, consectetur adipisicing elit, sed do eiusmod tempor incididunt ut labore et dolore magna aliqua.</p>
  <div class="abs social" style="left:140px;top:1154px">
    <span><i></i>snapverra</span><span><i></i>clipvane</span><span><i></i>Boardlyn</span>
  </div>
  <div class="photo" role="img" aria-label="Standing portrait of the coach in a white top and floral skirt" style="left:774px;top:786px;width:243px;height:501px;background:linear-gradient(180deg,#f4f4f4 0%,#d9c7bb 25%,#f2efec 45%,#4f6c8f 65%,#d9a58a 85%,#4f6c8f 100%)"></div>
</section>

<section>
  <h2 class="serif" style="left:0;width:1200px;text-align:center;top:1338px">Blog</h2>

  <h3 class="serif" style="left:140px;top:1507px">Lorem ipsum dolor</h3>
  <p class="abs body-copy" style="left:140px;top:1565px;width:345px">Lorem ipsum dolor sit amet, consectetur adipisicing elit, sed do eiusmod tempor incididunt ut labore et dolore magna aliqua. Ut enim ad minim veniam, quis nostrud exercitation ullamco laboris nisi ut aliquip ex ea commodo consequat.</p>
  <div class="btn" style="left:140px;top:1735px">READ MORE</div>
  <div class="photo" role="img" aria-label="The coach among coastal grasses by the water" style="left:536px;top:1469px;width:524px;height:367px;background:linear-gradient(180deg,#c9d4d8 0%,#a7b59a 45%,#8a9a5d 100%)"></div>

  <div class="photo" role="img" aria-label="The coach dancing in a blush dress by the sea" style="left:140px;top:1904px;width:524px;height:332px;background:linear-gradient(180deg,#dbe3e8 0%,#b9c9d2 55%,var(--blush) 75%,#8fb0b8 100%)"></div>
  <h3 class="serif" style="left:716px;top:1936px">Lorem ipsum dolor</h3>
  <p class="abs body-copy" style="left:716px;top:1991px;width:345px">Lorem ipsum dolor sit amet, consectetur adipisicing elit, sed do eiusmod tempor incididunt ut labore et dolore magna aliqua. Ut enim ad minim veniam, quis nostrud exercitation ullamco laboris nisi ut aliquip ex ea commodo consequat.</p>
  <div class="btn" style="left:716px;top:2162px">READ MORE</div>

  <h3 class="serif" style="left:140px;top:2350px">Lorem ipsum dolor</h3>
  <p class="abs body-copy" style="left:140px;top:2407px;width:345px">Lorem ipsum dolor sit amet, consectetur adipisicing elit, sed do eiusmod tempor incididunt ut labore et dolore magna aliqua. Ut enim ad minim veniam, quis nostrud exercitation ullamco laboris nisi ut aliquip ex ea commodo consequat.</p>
  <div class="btn" style="left:140px;top:2578px">READ MORE</div>
  <div class="photo" role="img" aria-label="The coach stretching on a beach facing a green island" style="left:536px;top:2309px;width:524px;height:369px;background:linear-gradient(180deg,#cfdbe4 0%,#a9c1d0 35%,#6f8c5a 48%,#9fc3cf 58%,var(--sand) 75%,#d8cfc2 100%)"></div>
</section>

<section>
  <div class="abs band" style="top:2839px;height:433px"></div>
  <h2 class="serif" style="left:144px;top:2925px;font-size:50px">My Podcast</h2>
  <p class="abs body-copy" style="left:142px;top:3008px;width:420px">Lorem ipsum dolor sit amet, consectetur adipisicing elit, sed do eiusmod tempor incididunt ut labore et dolore magna aliqua.</p>
  <div class="btn solid" style="left:140px;top:3119px">LISTEN TO PODCAST</div>
  <div class="photo" role="img" aria-label="Phone showing the podcast player with the coach's portrait" style="left:675px;top:2745px;width:374px;height:571px;border-radius:60px;transform:rotate(14deg);background:linear-gradient(180deg,#3a3a3a 0%,#ececec 12%,#c9b7ab 40%,#ffffff 60%,#ffffff 88%,#3a3a3a 100%)"></div>
</section>

<section>
  <h2 class="serif" style="left:0;width:1200px;text-align:center;top:3405px">#instatag</h2>
  <p class="abs body-copy" style="left:0;width:1200px;text-align:center;top:3507px">Lorem ipsum dolor sit amet, consectetur adipisicing elit, sed do<br>eiusmod tempor incididunt ut labore et dolore magna aliqua.</p>
  <div class="photo" role="img" aria-label="Woman in denim jacket before a flowered wall" style="left:140px;top:3627px;width:211px;height:209px;background:linear-gradient(180deg,#7a4a4a 0%,#b89484 50%,#33353c 100%)"></div>
  <div class="photo" role="img" aria-label="Mountain cabin above a snowy valley" style="left:376px;top:3627px;width:211px;height:209px;background:linear-gradient(160deg,#4e6673 0%,#c7c8c2 50%,#5a4a3c 100%)"></div>
  <div class="photo" role="img" aria-label="Rock arch on a beach under blue sky" style="left:614px;top:3627px;width:210px;height:209px;background:linear-gradient(180deg,#5f8bb0 0%,#c9d6df 40%,#c99a5e 60%,#d9d4cc 100%)"></div>
  <div class="photo" role="img" aria-label="Aerial view of turquoise sea with paddle boards" style="left:850px;top:3627px;width:210px;height:209px;background:linear-gradient(180deg,#e8f1f1 0%,#5ec3cc 35%,#1f9bb0 100%)"></div>
</section>

<section>
  <div class="abs band" style="top:4018px;height:415px"></div>
  <div class="photo" role="img" aria-label="Smiling portrait of the coach in a white top" style="left:108px;top:3956px;width:414px;height:477px;background:linear-gradient(180deg,#f4f4f4 0%,#3b2a22 20%,#c89a7e 45%,#ffffff 75%,#f1f1f1 100%)"></div>
  <h2 class="serif" style="left:588px;top:4098px;font-size:56px">Subscribe</h2>
  <p class="abs body-copy" style="left:586px;top:4182px;width:460px">Lorem ipsum dolor sit amet, consectetur adipisicing elit, sed do eiusmod tempor incididunt ut labore et dolore magna aliqua. Ut enim ad minim veniam.</p>
  <div class="field">YOUR E-MAIL ADRESS</div>
  <div class="btn solid" style="left:884px;top:4293px;width:184px;height:40px">SUBSCRIBE NOW</div>
</section>

<footer>
  <div class="abs footer"></div>
  <div class="abs footer-links">ABOUT<br>BLOG<br>PODCAST<br>SUBSCRIBE</div>
  <div class="abs social light" style="right:80px;top:4488px">
    <span><i></i>snapverra</span><span><i></i>clipvane</span><span><i></i>Boardlyn</span>
  </div>
</footer>

</body>
</html>
```